"The Plumeworks" nails, eyelash extensions and hair extensions. Need an eye catching design for bu

Need an eye catching design focusing on eyelash extensions, nail extensions and hair extensions. I like the colour green, black, glitter, pink?! need the design to be innovative and 'POP'. I'd like more emphasis on lashes and nails.
I'd like the business name and my phone number on the front of card.
Would really like something different and unique.
"The Plumeworks"
Nails, Eyelash & Hair Extensions
Mira
0417265903

Target Market(s)

20-40

Industry/Entity Type

Beauty Salon

Contact Information for Business Card

Id like my business name, My name and phone number on the front of card
"The Plumeworks".
Mira.
0417265903.
Id like some catchy design involving long lashes with possibly glitter, long hair and nails. Id like the lashes to be the first thing you see at first glance. I'm open to your creative flair. Just need the business card design to 'POP'! I like the colours green, black, pink, silver or gold glitter. wether it's pop art, 3d drawn pictures, isolated pics of lash, nails or hair, card design could be in black and white with isolated colours added..i'm open to your creative flair. use a font which stands out and easy to read.
(The back of the card will be used for writing appointment times.)

Font styles to use
Serif

Colors
6b449b
e667a6
25b39d

Requirements
Must have
• Long lashes, hair, nails.
• one sided
Nice to have
• bright catchy colours, innovative, uniqueness

```html
<!DOCTYPE html>
<html lang="en">
<head>
<meta charset="utf-8">
<title>The Plumeworks – Business Card</title>
<link rel="stylesheet" href="https://fonts.googleapis.com/css2?family=Cormorant+Garamond:wght@600&family=Libre+Baskerville&display=swap">
<style>
  :root {
    --purple: #6b449b;
    --teal: #25b39d;
    --gold: #c8962e;
    --white: #ffffff;
    --page: #ece8e4;
    --line: #7a4fa6;
    --ink-soft: #6d5a7e;
  }
  * { margin: 0; padding: 0; box-sizing: border-box; }
  html, body { width: 1200px; height: 900px; overflow: hidden; background: var(--page); }
  .canvas {
    position: relative; width: 1200px; height: 900px;
    display: flex; flex-direction: column; align-items: center; justify-content: center; gap: 48px;
  }
  .card {
    position: relative; width: 640px; height: 366px;
    border-radius: 18px; overflow: hidden; background: var(--white);
    box-shadow: 0 10px 28px rgba(60, 40, 70, 0.18);
  }
  .card svg { position: absolute; inset: 0; width: 100%; height: 100%; }
  .brand-name {
    font-family: "Cormorant Garamond", serif; font-weight: 600;
    color: var(--purple); line-height: 1; white-space: nowrap;
  }
  .brand-tagline {
    font-family: "Libre Baskerville", serif; white-space: nowrap;
  }
  /* front */
  .front .brand { position: absolute; left: 26px; top: 62px; }
  .front .brand-name { font-size: 40px; }
  .front .brand-tagline { font-size: 11.5px; color: var(--gold); margin-top: 8px; margin-left: 3px; }
  .front .contact {
    position: absolute; left: 30px; top: 308px;
    font-family: "Libre Baskerville", serif; font-size: 20px; color: var(--white); white-space: nowrap;
  }
  /* back */
  .back .brand { position: absolute; right: 50px; top: 58px; text-align: right; }
  .back .brand-name { font-size: 40px; }
  .back .brand-tagline { font-size: 11.5px; color: var(--teal); margin-top: 8px; }
  .appointment { position: absolute; left: 40px; right: 40px; top: 178px; }
  .appointment-row {
    height: 52px; border-bottom: 1.5px solid var(--line);
    display: flex; align-items: flex-end; padding-bottom: 6px;
    font-family: "Libre Baskerville", serif; font-size: 13px; color: var(--ink-soft);
  }
</style>
</head>
<body>
<main class="canvas">

  <section class="card front">
    <svg viewBox="0 0 640 366" preserveAspectRatio="none" aria-hidden="true">
      <defs>
        <clipPath id="photo-area">
          <path d="M404,0 L640,0 L640,366 L236,366 C324,300 384,160 404,0 Z"/>
        </clipPath>
        <linearGradient id="hair-tone" x1="0" y1="0" x2="1" y2="1">
          <stop offset="0" stop-color="#e9a56a"/><stop offset="1" stop-color="#b9602a"/>
        </linearGradient>
        <linearGradient id="eyes-tone" x1="0" y1="0" x2="1" y2="1">
          <stop offset="0" stop-color="#3a2a2c"/><stop offset="0.5" stop-color="#d9b3a3"/><stop offset="1" stop-color="#f1d9cf"/>
        </linearGradient>
        <linearGradient id="nails-tone" x1="0" y1="0" x2="1" y2="1">
          <stop offset="0" stop-color="#f4e4e6"/><stop offset="1" stop-color="#b89ac4"/>
        </linearGradient>
      </defs>
      <path class="teal-edge" fill="var(--teal)" d="M384,0 L404,0 C384,160 324,300 236,366 L212,366 C302,300 364,160 384,0 Z"/>
      <path class="purple-band" fill="var(--purple)" d="M0,366 L0,276 C150,250 310,170 362,0 L384,0 C364,160 302,300 212,366 Z"/>
      <g clip-path="url(#photo-area)">
        <polygon role="img" aria-label="Photo of long curled copper hair" fill="url(#hair-tone)" points="380,0 560,0 392,118 380,118"/>
        <polygon role="img" aria-label="Photo of eyes with long lash extensions" fill="url(#eyes-tone)" points="560,0 640,0 640,236 300,300 392,118"/>
        <polygon role="img" aria-label="Photo of hands with glitter purple nail extensions" fill="url(#nails-tone)" points="300,300 640,236 640,366 200,366"/>
      </g>
      <g stroke="var(--white)" stroke-width="4" clip-path="url(#photo-area)">
        <line x1="392" y1="118" x2="562" y2="0"/>
        <line x1="300" y1="300" x2="640" y2="236"/>
      </g>
    </svg>
    <div class="brand">
      <p class="brand-name">The Plumeworks</p>
      <p class="brand-tagline">Nails, Eyelash &amp; Hair Extensions</p>
    </div>
    <p class="contact">Mira : 0417265903</p>
  </section>

  <section class="card back">
    <svg viewBox="0 0 640 366" preserveAspectRatio="none" role="img" aria-label="Soft faded photo of hands with glitter purple nails">
      <defs>
        <radialGradient id="back-tone" cx="0.4" cy="0.6" r="0.8">
          <stop offset="0" stop-color="#ebe1ea"/><stop offset="0.6" stop-color="#f6f1f4"/><stop offset="1" stop-color="#fdfbfc"/>
        </radialGradient>
      </defs>
      <rect width="640" height="366" fill="url(#back-tone)"/>
    </svg>
    <div class="brand">
      <p class="brand-name">The Plumeworks</p>
      <p class="brand-tagline">Nails, Eyelash &amp; Hair Extensions</p>
    </div>
    <div class="appointment">
      <div class="appointment-row">Name :</div>
      <div class="appointment-row">Date :</div>
      <div class="appointment-row"></div>
    </div>
  </section>

</main>
</body>
</html>
```